Business Cards for Financial Service Consulting Business Ltd

Business Card Design for my risk management consultancy to the financial service industry
Responsible Lending, Fair Charges, Ethical Collections

Should be serious, professional, corporate

Target Market(s)

Fintech, Financial Services Industry

Industry/Entity Type

Financial Service

Contact Information for Business Card

Lewis Marsh
lew@slatewellconsulting.co.uk
07931520478
01632960417

Font styles to use
Serif

Colors

Designer to choose colors to be used in the design.

Requirements
Must have
• Name: Slatewell Consulting
• Logo, contact details
• The three pillars of my business Responsible Lending, Fair Charges, Ethical Collections
Nice to have
• Corporate Feel
Should not have
• jokes, pretty pictures, cartoons

```html
<!DOCTYPE html>
<html lang="en">
<head>
<meta charset="utf-8">
<title>Slatewell Consulting – Business Cards</title>
<link href="https://fonts.googleapis.com/css2?family=Montserrat:wght@500&family=Open+Sans:wght@400;600&display=swap" rel="stylesheet">
<style>
  :root {
    --backdrop: #2b2b2b;
    --card-dark: #262626;
    --card-dark-edge: #1a1a1a;
    --card-light: #f4f4f4;
    --ink: #1c1c1c;
    --ink-soft: #4a4a4a;
    --mark-on-dark: #9a9a9a;
    --pillar-text: #8a8a8a;
  }
  * { margin: 0; padding: 0; box-sizing: border-box; }
  html, body { width: 1200px; height: 716px; overflow: hidden; }
  body {
    background: var(--backdrop);
    font-family: "Open Sans", Arial, sans-serif;
    position: relative;
  }
  .card {
    position: absolute;
    top: 200px;
    width: 530px;
    height: 310px;
    border-radius: 22px;
  }
  .card--back {
    left: 40px;
    background: var(--card-dark);
    box-shadow: 0 6px 0 var(--card-dark-edge), 0 14px 30px rgba(0,0,0,.45);
  }
  .card--front {
    left: 630px;
    background: var(--card-light);
    box-shadow: 0 14px 30px rgba(0,0,0,.45);
    color: var(--ink);
  }
  .wordmark {
    font-family: "Montserrat", Arial, sans-serif;
    font-weight: 500;
    text-transform: uppercase;
    line-height: 1;
  }
  .wordmark__name { display: block; font-size: 40px; letter-spacing: 1px; }
  .wordmark__sub { display: block; font-size: 15px; letter-spacing: 11px; margin-top: 4px; }
  .card--back .wordmark {
    position: absolute; left: 0; right: 0; top: 92px;
    text-align: center; color: var(--mark-on-dark);
  }
  .pillars {
    position: absolute; left: 0; right: 0; top: 196px;
    text-align: center; font-size: 13px; color: var(--pillar-text);
  }
  .pillars .sep { margin: 0 10px; }
  .card--front .wordmark {
    position: absolute; right: 32px; top: 40px;
    text-align: right; color: var(--ink);
  }
  .card--front .wordmark__name { font-size: 34px; }
  .card--front .wordmark__sub { font-size: 13px; letter-spacing: 9px; }
  .holder { position: absolute; left: 34px; top: 150px; }
  .holder__name { font-size: 26px; font-weight: 400; line-height: 1.1; }
  .holder__title { font-size: 12px; color: var(--ink-soft); }
  .holder__rule {
    position: absolute; left: 34px; top: 196px;
    width: 190px; height: 2px; background: var(--ink);
  }
  .contacts {
    position: absolute; left: 34px; right: 30px; top: 210px;
    display: flex; justify-content: space-between;
    font-size: 13px; list-style: none;
  }
  .contacts li { display: flex; align-items: center; gap: 5px; }
  .contacts svg { width: 12px; height: 12px; fill: var(--ink); }
  .base-rule {
    position: absolute; left: 34px; right: 30px; top: 262px;
    height: 2px; background: var(--ink);
  }
</style>
</head>
<body>
  <section class="card card--back" aria-label="Card back">
    <div class="wordmark">
      <span class="wordmark__name">Slatewell</span>
      <span class="wordmark__sub">Consulting</span>
    </div>
    <p class="pillars">
      Responsible Lending<span class="sep">|</span>Fair Charges<span class="sep">|</span>Ethical Collections
    </p>
  </section>

  <section class="card card--front" aria-label="Card front">
    <div class="wordmark">
      <span class="wordmark__name">Slatewell</span>
      <span class="wordmark__sub">Consulting</span>
    </div>
    <div class="holder">
      <p class="holder__name">Lewis Marsh</p>
      <p class="holder__title">Job Title</p>
    </div>
    <div class="holder__rule"></div>
    <ul class="contacts">
      <li>
        <svg viewBox="0 0 12 12" aria-hidden="true"><path d="M1 4c0-2 2-3 5-3s5 1 5 3v1H8V4H4v1H1z M2 6h8l1 5H1z"/></svg>
        07931520478
      </li>
      <li>
        <svg viewBox="0 0 12 12" aria-hidden="true"><path d="M1 4c0-2 2-3 5-3s5 1 5 3v1H8V4H4v1H1z M2 6h8l1 5H1z"/></svg>
        01632960417
      </li>
      <li>
        <svg viewBox="0 0 12 12" aria-hidden="true"><path d="M0 2h12v8H0z" fill="none" stroke="#1c1c1c" stroke-width="1.4"/><path d="M0 2l6 5 6-5" fill="none" stroke="#1c1c1c" stroke-width="1.4"/></svg>
        lew@slatewellconsulting.co.uk
      </li>
    </ul>
    <div class="base-rule"></div>
  </section>
</body>
</html>
```